Emerging Australian photographer

I'm based in Cunderdin, a small rural town in the Wheatbelt area of Western Australia. So its a good thing that I love to travel further afield both for pleasure and for work. To me that is one and the same thing in any event!

My desire is to take photos that make the viewers heart skip. I love taking photos of people doing the things they love or being with the people they love. For me, the joy of photography comes with capturing the 'moments between the moments'. I like candid photography best of all - like when the new husband is staring joyfully at his bride and at that minute is unaware of the photographer capturing the moment.

I am available for weddings, engagements, birthdays, special events, newborns, family or individual portraits. By the end of the year I will be accredited with the Coastal Guild of Image Artisans.

I need a card that stands out but is elegant and would sit well on the table at a wedding or be given out in the church grounds. Classy and a little bit sassy.

Target Market(s)

Consumers who are seeking photographic services, eg wedding guests who see me at work and make enquiries.

Industry/Entity Type

Church

Contact Information for Business Card

Tamsin Bexley Photography
Tamsin Bexley
0452 307 618
www.tamsinbexley.com.au
photos@tamsinbexley.com.au

Requirements
Must have
• Must fit with the theme in the watermarks, but be crisp and modern.
Nice to have
• However it's not essential to have the pink! Facebook and Twitter logos.
Should not have
• Old style fonts like times new roman.

```html
<!DOCTYPE html>
<html lang="en">
<head>
<meta charset="utf-8">
<title>Tamsin Bexley Photography – Business Card</title>
<link href="https://fonts.googleapis.com/css2?family=Courgette&family=Arimo:wght@400&display=swap" rel="stylesheet">
<style>
  :root {
    --bg-top: #5c5c5c;
    --bg-bottom: #3e3e3e;
    --ink: #000000;
    --blush-light: #fdeef4;
    --blush-deep: #f6c6da;
    --rose: #e8559a;
    --rose-soft: #f4a9c9;
    --grey-mark: #6f6f6f;
    --grey-sub: #7a7a7a;
    --white: #ffffff;
    --script: "Courgette", cursive;
    --sans: "Arimo", Arial, sans-serif;
  }
  * { box-sizing: border-box; margin: 0; padding: 0; }
  html, body { width: 1200px; height: 1000px; overflow: hidden; }
  body {
    background: linear-gradient(180deg, var(--bg-top), var(--bg-bottom));
    font-family: var(--sans);
    position: relative;
  }
  .card {
    position: absolute;
    top: 329px;
    width: 555px;
    height: 342px;
    overflow: hidden;
    box-shadow: 0 2px 6px rgba(0,0,0,.45);
  }
  .card--front { left: 30px; }
  .card--back { left: 615px; background: var(--ink); }
  .card__art { position: absolute; inset: 0; width: 100%; height: 100%; }

  .front__name {
    position: absolute; top: 40px; left: 0; width: 555px; text-align: center;
    font-family: var(--script); font-size: 42px; color: var(--rose); line-height: 1;
  }
  .front__role {
    position: absolute; top: 95px; left: 0; width: 555px; text-align: center;
    font-size: 13px; color: var(--grey-sub);
  }
  .front__brand {
    position: absolute; left: 40px; top: 250px;
    font-family: var(--script); font-size: 26px; color: var(--grey-mark);
  }
  .contact-list {
    position: absolute; left: 278px; top: 208px; list-style: none;
  }
  .contact-list li {
    display: flex; align-items: center; gap: 10px;
    height: 21px; font-size: 14px; color: var(--white);
  }
  .contact-list svg { width: 13px; height: 13px; flex: none; }

  .back__brand {
    position: absolute; top: 160px; left: 0; width: 555px; text-align: center;
    font-family: var(--script); font-size: 36px; color: var(--grey-mark);
  }
</style>
</head>
<body>

<section class="card card--front" aria-label="Card front">
  <svg class="card__art" viewBox="0 0 555 342" preserveAspectRatio="none" aria-hidden="true">
    <defs>
      <linearGradient id="blushFront" x1="0" x2="1" y1="0" y2="0">
        <stop offset="0" stop-color="var(--blush-light)"/>
        <stop offset="1" stop-color="var(--blush-deep)"/>
      </linearGradient>
    </defs>
    <rect width="555" height="342" fill="url(#blushFront)"/>
    <path d="M0,72 C80,140 170,168 270,160 C380,150 470,140 555,232 L555,342 L0,342 Z" fill="var(--rose-soft)"/>
    <path d="M0,80 C80,148 170,176 270,166 C380,156 460,150 555,240 L555,342 L0,342 Z" fill="var(--rose)"/>
    <path d="M0,86 C80,154 170,182 270,172 C380,162 458,158 555,248 L555,342 L0,342 Z" fill="var(--ink)"/>
  </svg>
  <h1 class="front__name">tamsin bexley</h1>
  <p class="front__role">Owner, tb photography</p>
  <p class="front__brand">tamsin bexley</p>
  <ul class="contact-list">
    <li><svg viewBox="0 0 13 13"><rect width="13" height="13" rx="2" fill="var(--rose-soft)"/><rect x="4" y="2" width="5" height="9" rx="1" fill="var(--white)"/></svg>0452 307 618</li>
    <li><svg viewBox="0 0 13 13"><rect width="13" height="13" rx="2" fill="var(--rose-soft)"/><rect x="2.5" y="4" width="8" height="5.5" fill="var(--white)"/><path d="M2.5,4 L6.5,7 L10.5,4" stroke="var(--rose)" fill="none"/></svg>photos@tamsinbexley.com.au</li>
    <li><svg viewBox="0 0 13 13"><rect width="13" height="13" rx="2" fill="var(--rose-soft)"/><circle cx="6.5" cy="6.5" r="4" fill="none" stroke="var(--white)"/><path d="M2.5,6.5 H10.5 M6.5,2.5 V10.5" stroke="var(--white)"/></svg>www.tamsinbexley.com.au</li>
    <li><svg viewBox="0 0 13 13"><rect width="13" height="13" rx="2" fill="var(--rose-soft)"/></svg>tamsinbexley.</li>
    <li><svg viewBox="0 0 13 13"><rect width="13" height="13" rx="2" fill="var(--rose-soft)"/></svg>tamsinbexley.</li>
  </ul>
</section>

<section class="card card--back" aria-label="Card back">
  <svg class="card__art" viewBox="0 0 555 342" preserveAspectRatio="none" aria-hidden="true">
    <defs>
      <linearGradient id="blushBack" x1="0" x2="1" y1="0" y2="0">
        <stop offset="0" stop-color="var(--blush-light)"/>
        <stop offset="1" stop-color="var(--blush-deep)"/>
      </linearGradient>
    </defs>
    <path d="M0,182 C90,250 190,282 300,272 C400,262 470,232 555,298 L555,342 L0,342 Z" fill="var(--rose)"/>
    <path d="M0,190 C90,258 190,290 300,280 C400,270 468,242 555,306 L555,342 L0,342 Z" fill="var(--rose-soft)"/>
    <path d="M0,194 C90,262 190,294 300,284 C400,274 466,248 555,312 L555,342 L0,342 Z" fill="url(#blushBack)"/>
  </svg>
  <h2 class="back__brand">tamsin bexley photography</h2>
</section>

</body>
</html>
```